Brevanta needs a business Card Design

We are looking for a business card Design for our new Managed Service Provider Company, Brevanta. Brevanta encompasses everything IT for the average medium sized business. Our primary services are help desk support, cyber-security (malware and ransomware protection), and Disaster Recovery systems. We would like the design to have a very clean and professional look, with a very minimalist feel.

Target Market(s)

Medium to large sized businesses

Industry/Entity Type

It Service

Contact Information for Business Card

Name GoesHere
name@brevanta-mail.net
O: 555-382-6047
C: 555-000-0000

Font styles to use
Other font styles liked:
• Poppins Font Only Please

Colors

Designer to choose only greyscale colors for use in the design.

Requirements
Must have
• Logo included
Nice to have
• Cutting Edge, innovative, minimalistic, elegant

```html
<!DOCTYPE html>
<html lang="en">
<head>
<meta charset="UTF-8">
<title>Brevanta Business Card</title>
<link href="https://fonts.googleapis.com/css2?family=Poppins:wght@300;400;600&display=swap" rel="stylesheet">
<style>
  :root {
    --navy: #06243d;
    --paper: #ffffff;
    --backdrop: #e4e5e7;
    --ink: #0b2236;
    --muted: #5f6670;
    --rule: #2a3a4c;
  }
  * { margin: 0; padding: 0; box-sizing: border-box; }
  html, body {
    width: 1200px; height: 675px; overflow: hidden;
    background: var(--backdrop);
    font-family: "Poppins", sans-serif;
  }
  .stage {
    width: 1200px; height: 675px;
    display: flex; align-items: center; justify-content: center; gap: 40px;
  }
  .card {
    width: 520px; height: 297px; position: relative;
    box-shadow: 0 6px 18px rgba(0,0,0,0.18);
  }
  .card-front { background: var(--navy); }
  .card-back { background: var(--paper); }

  .front-wordmark {
    position: absolute; right: 48px; bottom: 70px;
    color: var(--paper); font-weight: 300; font-size: 26px;
    letter-spacing: 9px;
  }

  .back-brand {
    position: absolute; left: 44px; top: 0; bottom: 0; width: 230px;
    display: flex; align-items: center; justify-content: center;
  }
  .back-wordmark {
    color: var(--ink); font-weight: 300; font-size: 21px; letter-spacing: 7px;
  }
  .divider {
    position: absolute; left: 292px; top: 92px; width: 1px; height: 118px;
    background: var(--rule);
  }
  .contact {
    position: absolute; left: 312px; top: 88px; color: var(--ink);
  }
  .contact-name { font-weight: 600; font-size: 15px; line-height: 1.2; }
  .contact-role { font-weight: 300; font-size: 11px; color: var(--muted); margin-bottom: 14px; }
  .contact-line {
    display: flex; align-items: center; gap: 6px;
    font-weight: 400; font-size: 12px; line-height: 1.6;
  }
  .contact-line svg { width: 11px; height: 11px; fill: var(--ink); flex: none; }
</style>
</head>
<body>
<main class="stage">
  <section class="card card-front">
    <div class="front-wordmark">BREVANTA</div>
  </section>

  <section class="card card-back">
    <div class="back-brand">
      <div class="back-wordmark">BREVANTA</div>
    </div>
    <div class="divider"></div>
    <div class="contact">
      <div class="contact-name">JORDAN VALE</div>
      <div class="contact-role">Owner</div>
      <div class="contact-line">
        <svg viewBox="0 0 24 24"><path d="M6.6 10.8a15.1 15.1 0 0 0 6.6 6.6l2.2-2.2a1 1 0 0 1 1-.25 11.4 11.4 0 0 0 3.6.57 1 1 0 0 1 1 1V20a1 1 0 0 1-1 1A17 17 0 0 1 3 4a1 1 0 0 1 1-1h3.5a1 1 0 0 1 1 1c0 1.25.2 2.45.57 3.57a1 1 0 0 1-.25 1z"/></svg>
        <span>555-382-6047</span>
      </div>
      <div class="contact-line">
        <svg viewBox="0 0 24 24"><path d="M7 1h10a2 2 0 0 1 2 2v18a2 2 0 0 1-2 2H7a2 2 0 0 1-2-2V3a2 2 0 0 1 2-2zm0 3v14h10V4zm5 15.5a1 1 0 1 0 0 2 1 1 0 0 0 0-2z"/></svg>
        <span>555-000-0000</span>
      </div>
      <div class="contact-line">
        <svg viewBox="0 0 24 24"><path d="M2 5h20v14H2zm2 2v.5l8 5 8-5V7zm0 2.8V17h16V9.8l-8 5z"/></svg>
        <span>name@brevanta-mail.net</span>
      </div>
    </div>
  </section>
</main>
</body>
</html>
```